New business card for civil engineering company - "Keystone Audit"

We need a business card designed for our new structural engineering company.

The company name is "Keystone Audit" logo files attached.

We would like the following:
* Two-sided card
* Simple design

Information to be placed on the card:
Name - Marcus Dellow
Job Title - Director / Structural Engineer
Credentials - BEng(Hons), CPEng, CMengNZ, IntPE(NZ)
Email - marcus.dellow@keystoneaudit.co.nz
mobile - 0219364058
website - www.keystoneaudit.co.nz

```html
<!DOCTYPE html>
<html lang="en">
<head>
<meta charset="utf-8">
<title>Keystone Audit — Business Card</title>
<link rel="stylesheet" href="https://fonts.googleapis.com/css2?family=Open+Sans:wght@400;600;700&display=swap">
<style>
  :root {
    --backdrop: #d9d6d1;
    --card-black: #050505;
    --band-grey: #8a8a8a;
    --band-dark: #5e5e5e;
    --stripe-white: #f2f2f2;
    --text-white: #ffffff;
    --text-soft: #d8d8d8;
    --text-muted: #a9a9a9;
  }
  html, body {
    margin: 0;
    width: 1200px;
    height: 1024px;
    overflow: hidden;
    background: var(--backdrop);
    font-family: "Open Sans", Arial, sans-serif;
  }
  .card {
    position: absolute;
    left: 75px;
    top: 212px;
    width: 1050px;
    height: 600px;
    background: var(--card-black);
    overflow: hidden;
    box-shadow: 0 14px 40px rgba(0,0,0,0.35);
  }
  .card__band {
    position: absolute;
    inset: 0;
  }
  .brand {
    position: absolute;
    left: 70px;
    top: 300px;
    color: var(--text-white);
  }
  .brand__row {
    display: flex;
    align-items: center;
    gap: 14px;
  }
  .brand__mark {
    width: 22px;
    height: 22px;
    background: var(--text-soft);
  }
  .brand__name {
    font-size: 30px;
    font-weight: 600;
    letter-spacing: 2px;
    text-transform: uppercase;
  }
  .brand__tagline {
    margin-top: 6px;
    font-size: 11px;
    letter-spacing: 3.5px;
    color: var(--text-muted);
    text-transform: uppercase;
  }
  .divider {
    position: absolute;
    left: 395px;
    top: 110px;
    width: 2px;
    height: 250px;
    background: var(--text-white);
  }
  .contact {
    position: absolute;
    left: 440px;
    top: 95px;
    color: var(--text-white);
  }
  .contact__name {
    margin: 0;
    font-size: 32px;
    font-weight: 700;
    letter-spacing: 0.5px;
  }
  .contact__role,
  .contact__credentials {
    margin: 10px 0 0;
    font-size: 19px;
    color: var(--text-soft);
  }
  .contact__credentials { margin-top: 6px; }
  .contact__list {
    list-style: none;
    margin: 42px 0 0;
    padding: 0;
    font-size: 19px;
    color: var(--text-soft);
  }
  .contact__item {
    display: flex;
    align-items: center;
    gap: 12px;
    margin-bottom: 6px;
  }
  .contact__icon {
    width: 18px;
    height: 18px;
    flex: none;
  }
</style>
</head>
<body>
  <div class="card">
    <svg class="card__band" width="1050" height="600" viewBox="0 0 1050 600" aria-hidden="true">
      <path d="M 960 0 C 885 150 875 450 945 600 L 1050 600 L 1050 0 Z" fill="var(--band-grey)"/>
      <path d="M 1015 0 C 945 150 935 450 1000 600 L 1050 600 L 1050 0 Z" fill="var(--band-dark)" opacity="0.35"/>
      <path d="M 985 0 C 910 150 900 450 970 600" fill="none" stroke="var(--stripe-white)" stroke-width="8"/>
    </svg>

    <div class="brand">
      <div class="brand__row">
        <span class="brand__mark"></span>
        <span class="brand__name">Keystone Audit</span>
      </div>
      <div class="brand__tagline">Peer Review Specialists</div>
    </div>

    <div class="divider"></div>

    <div class="contact">
      <h1 class="contact__name">Marcus Dellow</h1>
      <p class="contact__role">Director / Structural Engineer</p>
      <p class="contact__credentials">BEng(Hons), CPEng, CMengNZ, IntPE(NZ)</p>
      <ul class="contact__list">
        <li class="contact__item">
          <svg class="contact__icon" viewBox="0 0 18 18" aria-hidden="true"><rect x="4" y="1" width="10" height="16" rx="1.5" fill="none" stroke="currentColor" stroke-width="1.6"/></svg>
          0219364058
        </li>
        <li class="contact__item">
          <svg class="contact__icon" viewBox="0 0 18 18" aria-hidden="true"><rect x="1" y="3" width="16" height="12" fill="currentColor"/><path d="M1 3 L9 10 L17 3" fill="none" stroke="#050505" stroke-width="1.5"/></svg>
          marcus.dellow@keystoneaudit.co.nz
        </li>
        <li class="contact__item">
          <svg class="contact__icon" viewBox="0 0 18 18" aria-hidden="true"><circle cx="9" cy="9" r="8" fill="currentColor"/><g fill="none" stroke="#050505" stroke-width="1"><ellipse cx="9" cy="9" rx="3.5" ry="8"/><line x1="1" y1="9" x2="17" y2="9"/><line x1="2.5" y1="5" x2="15.5" y2="5"/><line x1="2.5" y1="13" x2="15.5" y2="13"/></g></svg>
          www.keystoneaudit.co.nz
        </li>
      </ul>
    </div>
  </div>
</body>
</html>
```